BrightNook Software (a new software house) needs a Wordpress web site

We need a Wordpress web site. We develop innovative software as a service (on demand) for companies and cunsumers.
Updates

Reason: I need extra days to analyze.

Target Market(s)

Consumers who use mobile software to access useful information about your day by day in a crowd plataform and on demand.

Industry/Entity Type

Software

Requirements
Must have
• See wordpress template suggestion:
http://themes.plinvoa.com/?theme=marmot

```html
<!DOCTYPE html>
<html lang="en">
<head>
<meta charset="utf-8">
<title>BrightNook Software</title>
<link href="https://fonts.googleapis.com/css2?family=Open+Sans:wght@400;600&family=Oswald:wght@300;400&family=Roboto+Condensed:wght@400&display=swap" rel="stylesheet">
<style>
:root{
  --ink:#333;
  --muted:#555;
  --accent:#6f8bd0;
  --hero:#7a8fc8;
  --hero-deep:#6a7fbd;
  --band:#4f63a0;
  --caption:#1e1e1e;
  --box:#f1f0f0;
  --rule:#d6d6d6;
  --footer:#e3e3e3;
}
*{margin:0;padding:0;box-sizing:border-box}
html,body{width:1000px;height:1200px;overflow:hidden;background:#fff}
body{position:relative;font-family:"Open Sans",Arial,sans-serif;color:var(--ink)}
.abs{position:absolute}

.site-header{left:0;top:0;width:1000px;height:79px;background:#fff}
.brand{left:100px;top:24px;display:flex;align-items:center;gap:10px}
.brand-dot{width:30px;height:30px;border-radius:50%;background:#222}
.brand-name{font-family:"Open Sans",sans-serif;font-weight:600;font-size:20px;color:#222}
.nav{top:32px;left:0;font-family:"Open Sans",sans-serif;font-size:11px;color:#333}
.nav a{position:absolute;white-space:nowrap;text-decoration:none;color:inherit}
.nav a.active{color:var(--accent)}

.hero{left:0;top:79px;width:1000px;height:363px;background:linear-gradient(180deg,var(--hero) 0%,var(--hero) 72%,var(--hero-deep) 100%)}
.hero-art{left:100px;top:25px;width:367px;height:313px;border-radius:8px;background:radial-gradient(ellipse at 50% 40%,#bfe6ff 0%,#3e9be6 40%,rgba(106,127,189,0) 72%)}
.hero-title{left:502px;top:75px;font-family:"Oswald",sans-serif;font-weight:300;color:#fff;font-size:38px;line-height:40px;letter-spacing:.5px}
.hero-text{left:502px;top:213px;width:400px;font-family:"Roboto Condensed",sans-serif;color:#fff;font-size:14.5px;line-height:20px}
.hero-band{left:0;top:442px;width:1000px;height:22px;background:var(--band)}
.dot{top:450px;width:8px;height:8px;border-radius:50%;background:#aab3cc}
.dot.on{background:#333}

.section-title{font-family:"Open Sans",sans-serif;font-size:15px;color:#555;background:#fff;padding-right:14px}
.hatch{height:6px;background:repeating-linear-gradient(115deg,#bdbdbd 0 1px,transparent 1px 3px)}

.card{width:250px;height:169px}
.card-media{width:250px;height:133px}
.card-caption{position:absolute;left:0;bottom:0;width:250px;height:36px;background:var(--caption);color:#fff;padding:3px 10px}
.card-caption h3{font-weight:400;font-size:12.5px;line-height:16px}
.card-caption p{font-size:10.5px;line-height:15px}

.feature{width:258px;height:97px;background:var(--box);padding:13px 5px 0 4px}
.feature-head{display:flex;align-items:center;gap:8px;padding:0 4px 7px;border-bottom:1px solid var(--rule);font-family:"Roboto Condensed",sans-serif;color:var(--accent);font-size:14px}
.feature p{margin-top:10px;font-size:10.8px;line-height:14px;color:var(--muted);text-align:justify}

.site-footer{left:0;top:1152px;width:1000px;height:48px;background:var(--footer)}
.copyright{left:99px;top:1172px;font-size:10px;color:#444;font-family:Arial,sans-serif}
.social{top:1164px;width:27px;height:27px;border-radius:50%}
</style>
</head>
<body>

<header class="site-header abs">
  <div class="brand abs"><span class="brand-dot"></span><span class="brand-name">BrightNook Software</span></div>
  <nav class="nav abs">
    <a class="active" style="left:462px">HOME</a>
    <a style="left:527px">SERVICES</a>
    <a style="left:608px">PROJECTS</a>
    <a style="left:693px">FEATURES</a>
    <a style="left:779px">BLOG</a>
    <a style="left:841px">CONTACT</a>
  </nav>
</header>

<section class="hero abs">
  <div class="hero-art abs" role="img" aria-label="Three glowing blue light bulbs"></div>
  <h1 class="hero-title abs">WE DEVELOP<br>INNOVATIVE SOFTWARE<br>AS A SERVICE</h1>
  <p class="hero-text abs">Nulla tincidunt ultricies sodales. Pellentesque sed nisl mauris, sit amet sodales sem.Lorem ipsum dolor sit amet, consectetur adipiscing elit.Quisque dictum arcu sagittis tellus scelerisque venenatis at nec dui. Aliquam</p>
</section>
<div class="hero-band abs"></div>
<span class="dot abs" style="left:483px"></span>
<span class="dot on abs" style="left:496px"></span>
<span class="dot abs" style="left:509px"></span>

<div class="hatch abs" style="left:233px;top:487px;width:667px"></div>
<h2 class="section-title abs" style="left:100px;top:480px">RECENT PROJECTS</h2>

<article class="card abs" style="left:100px;top:523px">
  <div class="card-media" role="img" aria-label="Woman looking at hexagonal technology screens" style="background:linear-gradient(90deg,#c9b6a6,#dfe6f3 35%,#c7d3ea)"></div>
  <div class="card-caption"><h3>Lorem ipsum dolor sit amet</h3><p>arcu sagittis tellusconsectetur adipiscing elit.</p></div>
</article>
<article class="card abs" style="left:375px;top:523px">
  <div class="card-media" role="img" aria-label="Hand holding a smartphone with a weather app" style="background:linear-gradient(135deg,#e8e8e8,#9a9a9a 55%,#4a3a30)"></div>
  <div class="card-caption"><h3>Lorem ipsum dolor sit amet</h3><p>arcu sagittis tellusconsectetur adipiscing elit.</p></div>
</article>
<article class="card abs" style="left:650px;top:523px">
  <div class="card-media" role="img" aria-label="World map made of puzzle pieces" style="background:linear-gradient(135deg,#f2f5f8,#6f93b5 50%,#eef2f6)"></div>
  <div class="card-caption"><h3>Lorem ipsum dolor sit amet</h3><p>arcu sagittis tellusconsectetur adipiscing elit.</p></div>
</article>

<div class="hatch abs" style="left:100px;top:734px;width:333px"></div>
<div class="hatch abs" style="left:563px;top:734px;width:336px"></div>
<h2 class="abs" style="left:440px;top:724px;font-family:'Roboto Condensed',sans-serif;font-weight:400;font-size:20px;color:#555">WHAT WE DO</h2>

<div class="feature abs" style="left:100px;top:771px">
  <div class="feature-head"><svg width="12" height="14" viewBox="0 0 12 14"><rect x="1" y="0.5" width="10" height="13" rx="2" fill="#222"/><rect x="3" y="2.5" width="6" height="8" fill="#fff"/></svg>APPS MODULE</div>
  <p>Nulla tincidunt ultricies sodales. Pellentesque sed nisl mauris, sit amet sodales sem.nisl mauris, sit amet sodales sem.</p>
</div>
<div class="feature abs" style="left:372px;top:771px">
  <div class="feature-head"><svg width="12" height="14" viewBox="0 0 12 14"><circle cx="6" cy="5" r="4.5" fill="#222"/><rect x="4" y="9" width="4" height="4" fill="#222"/></svg>INNOVATIVE</div>
  <p>Nulla tincidunt ultricies sodales. Pellentesque sed nisl mauris, sit amet sodales sem.nisl mauris, sit amet sodales sem.</p>
</div>
<div class="feature abs" style="left:642px;top:771px">
  <div class="feature-head"><svg width="14" height="14" viewBox="0 0 14 14"><circle cx="7" cy="7" r="6.5" fill="#222"/><circle cx="7" cy="7" r="2.5" fill="#fff"/><path d="M2 2L12 12M12 2L2 12" stroke="#fff" stroke-width="1.3"/></svg>SUPPORT MULTI LANGUAGES</div>
  <p>Nulla tincidunt ultricies sodales. Pellentesque sed nisl mauris, sit amet sodales sem.nisl mauris, sit amet sodales sem.</p>
</div>

<div class="hatch abs" style="left:203px;top:918px;width:697px"></div>
<h2 class="section-title abs" style="left:100px;top:911px">RECENT POSTS</h2>

<article class="card abs" style="left:100px;top:954px">
  <div class="card-media" role="img" aria-label="Laptop beside a glowing globe" style="background:linear-gradient(135deg,#dfe5f3,#7f93c6 55%,#eef1f8)"></div>
  <div class="card-caption"><h3>Lorem ipsum dolor sit amet</h3><p>arcu sagittis tellusconsectetur adipiscing elit.</p></div>
</article>
<article class="card abs" style="left:375px;top:954px">
  <div class="card-media" role="img" aria-label="Golden globe with a hand" style="background:linear-gradient(135deg,#8a6a1c,#e9c957 50%,#f4e7b6)"></div>
  <div class="card-caption"><h3>Lorem ipsum dolor sit amet</h3><p>arcu sagittis tellusconsectetur adipiscing elit.</p></div>
</article>
<article class="card abs" style="left:650px;top:954px">
  <div class="card-media" role="img" aria-label="Hands typing on a keyboard" style="background:linear-gradient(160deg,#e6e8ec,#9aa0a8 50%,#3a3d44)"></div>
  <div class="card-caption"><h3>Lorem ipsum dolor sit amet</h3><p>arcu sagittis tellusconsectetur adipiscing elit.</p></div>
</article>

<footer class="site-footer abs"></footer>
<p class="copyright abs">© 2013 halvern-studio | &nbsp;All Rights Reserved.</p>
<span class="social abs" style="left:764px;background:#3b5998" aria-label="Social link"></span>
<span class="social abs" style="left:798px;background:#2fa7e0" aria-label="Social link"></span>
<span class="social abs" style="left:834px;background:#d8342a" aria-label="Social link"></span>
<span class="social abs" style="left:868px;background:#e64534" aria-label="Social link"></span>

</body>
</html>
```